Bar Tundrel Menu

We are a new bar in Lower East Side in NYC. The name is Bar Tundrel and we need to create a design for our craft cocktails and food menu. Bar Tundrel is an innovative, laid back, yet elegant American cocktail bar with a slight Russian accent. The theme is icy coolness, with silver and gray accents throughout the décor and features cool but not harsh lighting.

```html
<!DOCTYPE html>
<html lang="en">
<head>
<meta charset="utf-8">
<title>Bar Tundrel Menu</title>
<link rel="stylesheet" href="https://fonts.googleapis.com/css2?family=Tinos:wght@400;700&display=swap">
<style>
  :root {
    --backdrop: #e6e6e6;
    --ink: #1e1814;
    --food-top: #e2401a;
    --food-mid: #ee6a1f;
    --food-low: #f39a2a;
    --drink-top: #e0241b;
    --drink-mid: #f46a16;
    --drink-low: #fbd61e;
    --rule: #2b211b;
  }
  * { box-sizing: border-box; margin: 0; padding: 0; }
  html, body { width: 1200px; height: 841px; overflow: hidden; }
  body {
    background: var(--backdrop);
    font-family: "Tinos", "Times New Roman", serif;
    color: var(--ink);
    display: flex;
    align-items: center;
    justify-content: center;
    gap: 21px;
  }
  .menu-card {
    width: 390px;
    height: 696px;
    position: relative;
    box-shadow: 0 2px 6px rgba(0,0,0,0.25);
  }
  .food-menu {
    background:
      radial-gradient(ellipse at 70% 30%, rgba(255,180,60,0.35), transparent 60%),
      radial-gradient(ellipse at 20% 75%, rgba(255,170,50,0.4), transparent 55%),
      linear-gradient(170deg, var(--food-top), var(--food-mid) 50%, var(--food-low));
    padding: 38px 24px 0;
    text-align: center;
  }
  .brand-name {
    font-size: 44px;
    font-weight: 700;
    letter-spacing: 2px;
    line-height: 1;
  }
  .menu-heading {
    font-size: 22px;
    font-weight: 700;
    margin-top: 12px;
    margin-bottom: 26px;
  }
  .dish { margin-bottom: 26px; }
  .dish-name { font-size: 18.5px; font-weight: 700; line-height: 1.15; }
  .dish-notes { font-size: 11px; margin-top: 3px; }
  .dessert-rule {
    border: none;
    border-top: 2px dashed var(--rule);
    margin: 2px 10px 22px;
  }
  .drinks-menu {
    background:
      radial-gradient(ellipse at 80% 65%, rgba(255,240,120,0.5), transparent 50%),
      linear-gradient(180deg, var(--drink-top), var(--drink-mid) 45%, var(--drink-low) 85%);
    padding: 6px 10px 0;
    text-align: center;
  }
  .drinks-heading { font-size: 17.5px; font-weight: 700; letter-spacing: 0.3px; }
  .corner-brand {
    position: absolute;
    top: 30px;
    right: 12px;
    font-size: 12px;
    font-weight: 700;
  }
  .cocktail-list { list-style: none; margin-top: 2px; }
  .cocktail { height: 35.6px; }
  .cocktail-name { font-size: 14.5px; font-weight: 700; line-height: 1.3; }
  .cocktail-notes { font-size: 6.8px; line-height: 1.2; }
</style>
</head>
<body>
  <section class="menu-card food-menu">
    <h1 class="brand-name">Bar Tundrel</h1>
    <h2 class="menu-heading">MENU</h2>
    <div class="dish"><div class="dish-name">ROYAL OSSETRA CAVIAR-----$40</div></div>
    <div class="dish"><div class="dish-name">OYSTER SHOOTER’S-----$15</div><div class="dish-notes">Vodka , Alaskan Mix , Lime</div></div>
    <div class="dish"><div class="dish-name">SALMON TARTARE-----$15</div><div class="dish-notes">Mango ,Avocado , Lemon Vinaigrette , Dill</div></div>
    <div class="dish"><div class="dish-name">ROASTED BEET SALAD-----$12</div><div class="dish-notes">Horseradish Cream , Toasted Pecans , Blue Cheese</div></div>
    <div class="dish"><div class="dish-name">ALASKAN KING CRAB TACO-----$18</div><div class="dish-notes">Cabbage Salad, Chili Mayo , Avocado Mousse</div></div>
    <div class="dish"><div class="dish-name">ROAST BEEF CROSTINI-----$ 12</div><div class="dish-notes">Caramelized Onion , Red Wine Sauce , Dijon Mustard</div></div>
    <div class="dish"><div class="dish-name">LOBSTER MAC &amp; CHEESE-----$18</div><div class="dish-notes">White Cheddar , Truffle , Herb Bread Crums</div></div>
    <div class="dish"><div class="dish-name">GRILLED CHEESE BITES-----$18</div><div class="dish-notes">Smoked Ham, Gruyere Cheese, Truffle Butter</div></div>
    <hr class="dessert-rule">
    <div class="dish"><div class="dish-name">CHOCOLATE CAKE-----$10</div><div class="dish-notes">Vanilla Cream &amp; Strawberry Mint</div></div>
  </section>

  <section class="menu-card drinks-menu">
    <h2 class="drinks-heading">SIGNATURE COCKTAILS $15</h2>
    <div class="corner-brand">Bar Tundrel</div>
    <ul class="cocktail-list">
      <li class="cocktail"><div class="cocktail-name">Martini Imperial</div><div class="cocktail-notes">(Vodka, Birch Tree Juice, Dry Vermouth)</div></li>
      <li class="cocktail"><div class="cocktail-name">Molotov Cocktail</div><div class="cocktail-notes">(Vodka, Espresso Syrup, Toasted Caraway Whipped Cream)</div></li>
      <li class="cocktail"><div class="cocktail-name">The Musher</div><div class="cocktail-notes">(Gin, Bitter Aperitif, Ginger Juice, Lime Juice, Honey Syrup, Cucumber, Raspberry and Basil)</div></li>
      <li class="cocktail"><div class="cocktail-name">Northern Lights</div><div class="cocktail-notes">(Light Rum, Orgeat, Lime Juice, Kiwi, Butterfly Pea Tea Syrup)</div></li>
      <li class="cocktail"><div class="cocktail-name">Lost Surfer</div><div class="cocktail-notes">(Rhum Agricole, Cherry Liqueur, Maple Syrup, Lime Juice, Aromatic Bitters, Pineapple)</div></li>
      <li class="cocktail"><div class="cocktail-name">Seward’s Folly</div><div class="cocktail-notes">(Islay Scotch, Dry Vermouth, Pear Compote, Spiced Cherry Bitters, Smoke Bitters)</div></li>
      <li class="cocktail"><div class="cocktail-name">From Folly to Fortune</div><div class="cocktail-notes">(Bitter Liqueur, Americano Bianco, Blanc Aperitif, Orange Bitters)</div></li>
      <li class="cocktail"><div class="cocktail-name">Anchorage 76</div><div class="cocktail-notes">(Vodka, Elderflower Syrup, Lemon Juice, Champagne)</div></li>
      <li class="cocktail"><div class="cocktail-name">Cold, Cold Heart</div><div class="cocktail-notes">(Dill Infused Vodka, Beet Syrup, Lemon Juice, Celery Bitters)</div></li>
      <li class="cocktail"><div class="cocktail-name">Back to our Roots</div><div class="cocktail-notes">(Rye Vodka, Carrot Juice, Ginger Syrup, Lemon Juice, Tiki Bitters)</div></li>
      <li class="cocktail"><div class="cocktail-name">Ancient Spirits</div><div class="cocktail-notes">(Aged Aquavit, Honey Liqueur, Cardamom Bitters)</div></li>
      <li class="cocktail"><div class="cocktail-name">Denali Sunset</div><div class="cocktail-notes">(Dry Gin, Coconut Syrup, Lemon Juice, Egg White, Rosehip Tea)</div></li>
      <li class="cocktail"><div class="cocktail-name">¿Por K-Vas?</div><div class="cocktail-notes">(Silver Tequila, Lime Juice, Serrano Infused Agave Nectar, Kvass)</div></li>
      <li class="cocktail"><div class="cocktail-name">Alaskan Mule</div><div class="cocktail-notes">(Vodka, Cherry Shrub, Lime Juice, Ginger Beer)</div></li>
      <li class="cocktail"><div class="cocktail-name">Forget-Me-Not</div><div class="cocktail-notes">(Botanical Gin, Blanc Aperitif, Lemon Juice, Strawberry Syrup, Egg White)</div></li>
      <li class="cocktail"><div class="cocktail-name">The Torch</div><div class="cocktail-notes">(Small Batch Bourbon, Fernet, Blanc Vermouth, Mango Puree)</div></li>
      <li class="cocktail"><div class="cocktail-name">Spice Trader</div><div class="cocktail-notes">(Rye, Light Rum, Extra Dry Vermouth, Orange Juice, Spiced Honey Syrup, Chamomile, Smoke Bitters and New Orleans Bitters)</div></li>
      <li class="cocktail"><div class="cocktail-name">Beyond the Border</div><div class="cocktail-notes">(Mezcal, Pear Puree, Lime Juice, Agave Nectar, Rosemary, Black Walnut Bitters)</div></li>
    </ul>
  </section>
</body>
</html>
```